Student Card

we are college and require a student card which we issue on enlroment to students, just like a univeristy.

Baisic information need to be placed is:
Student photo
student ID
date of birth
exp date

our college contact details on the rear
its a tool for branding so its important the theme is in line with our colours and logo, please view our website www.harlowmereinstitute.net.au

Industry/Entity Type

College

```html
<!DOCTYPE html>
<html lang="en">
<head>
<meta charset="utf-8">
<title>Harlowmere Institute – Student Identity Card</title>
<link rel="stylesheet" href="https://fonts.googleapis.com/css2?family=Barlow:wght@300;400;600&display=swap">
<style>
  :root {
    --card-mint: #84fbe2;
    --card-mint-light: #c9fff1;
    --brand-blue: #2f4bf0;
    --ink: #111111;
    --photo-fill: #e5eded;
  }
  html, body {
    margin: 0;
    padding: 0;
    overflow: hidden;
    background: #ffffff;
  }
  .id-card {
    position: relative;
    width: 1200px;
    height: 733px;
    background: var(--card-mint);
    overflow: hidden;
    font-family: "Barlow", sans-serif;
  }
  .card-decoration {
    position: absolute;
    left: 760px;
    top: 140px;
    width: 440px;
    height: 593px;
  }
  .card-heading {
    position: absolute;
    left: 53px;
    top: 40px;
    margin: 0;
    line-height: 1;
  }
  .college-name {
    display: block;
    font-size: 56px;
    font-weight: 600;
    color: var(--brand-blue);
    letter-spacing: -0.5px;
  }
  .card-title {
    display: block;
    margin-top: 10px;
    font-size: 68px;
    font-weight: 300;
    color: var(--ink);
    letter-spacing: -0.5px;
  }
  .brand-mark {
    position: absolute;
    left: 990px;
    top: 40px;
    width: 170px;
    text-align: center;
  }
  .brand-mark-dot {
    display: block;
    width: 48px;
    height: 48px;
    margin: 0 auto 8px;
    border-radius: 50%;
    background: var(--brand-blue);
  }
  .brand-mark-name {
    font-size: 13px;
    font-weight: 600;
    color: var(--brand-blue);
    letter-spacing: 1px;
    text-transform: uppercase;
  }
  .photo-slot {
    position: absolute;
    left: 53px;
    top: 231px;
    width: 355px;
    height: 456px;
    box-sizing: border-box;
    background: var(--photo-fill);
    border: 3px dotted var(--ink);
  }
  .student-details {
    position: absolute;
    left: 478px;
    top: 226px;
    margin: 0;
  }
  .detail-label,
  .detail-value {
    margin: 0;
    font-size: 44px;
    line-height: 50px;
    font-weight: 400;
    letter-spacing: 0.5px;
  }
  .detail-label {
    color: var(--brand-blue);
  }
  .detail-value {
    color: var(--ink);
    margin-bottom: 23px;
  }
</style>
</head>
<body>
  <main class="id-card">
    <svg class="card-decoration" role="img" aria-label="Faint outline of a kangaroo, the college mascot" viewBox="0 0 440 593" preserveAspectRatio="none">
      <defs>
        <radialGradient id="mascot-glow" cx="55%" cy="55%" r="60%">
          <stop offset="0%" stop-color="var(--card-mint-light)" stop-opacity="0.55"/>
          <stop offset="100%" stop-color="var(--card-mint)" stop-opacity="0"/>
        </radialGradient>
      </defs>
      <rect width="440" height="593" fill="url(#mascot-glow)"/>
    </svg>

    <h1 class="card-heading">
      <span class="college-name">Harlowmere Institute</span>
      <span class="card-title">Student Identity Card</span>
    </h1>

    <div class="brand-mark">
      <span class="brand-mark-dot"></span>
      <span class="brand-mark-name">Harlowmere Institute</span>
    </div>

    <div class="photo-slot" aria-label="Student photo"></div>

    <dl class="student-details">
      <dt class="detail-label">NAME</dt>
      <dd class="detail-value">A.N OTHER</dd>
      <dt class="detail-label">STUDENT ID NUMBER</dt>
      <dd class="detail-value">123456789</dd>
      <dt class="detail-label">DATE OF BIRTH</dt>
      <dd class="detail-value">01/01/1901</dd>
      <dt class="detail-label">EXP DATE</dt>
      <dd class="detail-value">01/01/1901</dd>
    </dl>
  </main>
</body>
</html>
```